Tirovel

We need a business card for our company is a holding for different business all are different we try to have some air of relax and fun in our projects we add pictures of the office to give you an idea od the mood of the business

Business

```html
<!DOCTYPE html>
<html lang="en">
<head>
<meta charset="utf-8">
<title>Tirovel — Business Card</title>
<link rel="stylesheet" href="https://fonts.googleapis.com/css2?family=Exo+2:wght@400;600&display=swap">
<style>
  :root {
    --backdrop: #e9e6e1;
    --card: #ffffff;
    --brand-yellow: #f5e62a;
    --ink-brown: #4a3b32;
    --ink-soft: #5c5049;
    --rule-grey: #b9b4ae;
  }
  * { margin: 0; padding: 0; box-sizing: border-box; }
  html, body {
    width: 1200px; height: 899px; overflow: hidden;
    background: var(--backdrop);
    font-family: "Exo 2", sans-serif;
  }
  .canvas { position: relative; width: 1200px; height: 899px; }
  .card {
    position: absolute; left: 100px; top: 165px;
    width: 1000px; height: 570px;
    background: var(--card);
    border-radius: 56px;
    overflow: hidden;
    box-shadow: 0 12px 40px rgba(0,0,0,0.12);
  }
  .brand {
    position: absolute; left: 90px; top: 150px;
    display: flex; align-items: center; gap: 22px;
  }
  .brand-square { width: 70px; height: 70px; background: var(--brand-yellow); }
  .brand-name {
    font-weight: 600; font-size: 74px; color: var(--ink-brown);
    letter-spacing: -1px; line-height: 1;
  }
  .details { position: absolute; left: 520px; top: 72px; color: var(--ink-brown); }
  .person-name { font-weight: 400; font-size: 34px; letter-spacing: 2px; text-transform: uppercase; }
  .person-role { font-size: 22px; margin-top: 2px; color: var(--ink-soft); }
  .address { font-size: 24px; line-height: 1.4; margin-top: 52px; letter-spacing: 0.5px; }
  .contacts { list-style: none; margin-top: 40px; }
  .contacts li {
    display: flex; align-items: center; gap: 14px;
    font-size: 18px; color: var(--ink-soft); height: 30px; letter-spacing: 1px;
  }
  .contacts svg { width: 18px; height: 18px; fill: var(--ink-brown); }
  .swoosh { position: absolute; left: 0; bottom: 0; width: 1000px; height: 570px; }
  .website {
    position: absolute; left: 200px; bottom: 44px;
    font-size: 19px; letter-spacing: 3px; color: var(--ink-brown);
    transform: rotate(3deg); transform-origin: left center;
  }
</style>
</head>
<body>
<div class="canvas">
  <div class="card">
    <svg class="swoosh" viewBox="0 0 1000 570" aria-hidden="true">
      <path d="M0 452 Q480 500 1000 520" fill="none" stroke="var(--rule-grey)" stroke-width="3"/>
      <path d="M0 462 Q480 510 1000 530 L1000 570 L0 570 Z" fill="var(--brand-yellow)"/>
    </svg>

    <div class="brand">
      <span class="brand-square"></span>
      <span class="brand-name">Tirovel</span>
    </div>

    <div class="details">
      <p class="person-name">Marcus Delane</p>
      <p class="person-role">Managing Director</p>
      <p class="address">412 9th floor, Harbor Crest<br>Road WPK</p>
      <ul class="contacts">
        <li><svg viewBox="0 0 24 24"><path d="M6.6 10.8a15 15 0 0 0 6.6 6.6l2.2-2.2a1 1 0 0 1 1-.25 11.4 11.4 0 0 0 3.6.57 1 1 0 0 1 1 1V20a1 1 0 0 1-1 1A17 17 0 0 1 3 4a1 1 0 0 1 1-1h3.5a1 1 0 0 1 1 1c0 1.25.2 2.45.57 3.57a1 1 0 0 1-.25 1z"/></svg>010 555 0147</li>
        <li><svg viewBox="0 0 24 24"><path d="M7 1h10a2 2 0 0 1 2 2v18a2 2 0 0 1-2 2H7a2 2 0 0 1-2-2V3a2 2 0 0 1 2-2zm0 3v14h10V4zm5 15.5a1.2 1.2 0 1 0 0 2.4 1.2 1.2 0 0 0 0-2.4z"/></svg>010 555 0148</li>
        <li><svg viewBox="0 0 24 24"><path d="M6 2h9l3 3v5h2a2 2 0 0 1 2 2v8a2 2 0 0 1-2 2H4a2 2 0 0 1-2-2v-8a2 2 0 0 1 2-2h2zm2 2v6h8V6h-2V4zm-2 10v2h4v-2z"/></svg>010 555 0149</li>
        <li><svg viewBox="0 0 24 24"><path d="M2 5h20v14H2zm2 2v.5l8 5 8-5V7zm0 2.8V17h16V9.8l-8 5z"/></svg>hello@tirovelmail.com</li>
        <li><svg viewBox="0 0 24 24"><path d="M12 2a10 10 0 1 0 0 20 10 10 0 0 0 0-20zm6.9 9h-3a15 15 0 0 0-1.3-5.3A8 8 0 0 1 18.9 11zM12 4.1c.9 1.2 1.7 3.6 1.9 6.9h-3.8c.2-3.3 1-5.7 1.9-6.9zM9.4 5.7A15 15 0 0 0 8.1 11h-3a8 8 0 0 1 4.3-5.3zM5.1 13h3a15 15 0 0 0 1.3 5.3A8 8 0 0 1 5.1 13zm6.9 6.9c-.9-1.2-1.7-3.6-1.9-6.9h3.8c-.2 3.3-1 5.7-1.9 6.9zm2.6-1.6a15 15 0 0 0 1.3-5.3h3a8 8 0 0 1-4.3 5.3z"/></svg>www.tirovelgroup.com</li>
      </ul>
    </div>

    <p class="website">www.tirovelgroup.com</p>
  </div>
</div>
</body>
</html>
```